Trevik Builders Business Card Design Project

Clean sharp business card
Ability to write on back of card
Details for the card -
Address: PO Box 5087, Corrowen, Qld, 4652
ABN: 47 305 921 276
BSA LIC 6825170
Ph: 07 4651 2839
Fax: 07 4651 2840
Email: trevikbuilders@quillpost.net

Reason: Time to review designs after weekend

```html
<!DOCTYPE html>
<html lang="en">
<head>
<meta charset="utf-8">
<title>Trevik Builders – Business Card</title>
<link rel="stylesheet" href="https://fonts.googleapis.com/css2?family=Arimo:wght@400;700&display=swap">
<style>
  :root {
    --bg: #e9e7e3;
    --card: #ffffff;
    --card-shade: #eeeeee;
    --orange: #ee7d1e;
    --orange-deep: #d96a10;
    --ink: #3a3a3a;
    --grey: #6b6b6b;
    --black: #141414;
  }
  * { box-sizing: border-box; margin: 0; padding: 0; }
  html, body { width: 1200px; height: 1023px; overflow: hidden; }
  body {
    background: var(--bg);
    font-family: "Arimo", Arial, sans-serif;
    color: var(--ink);
    display: flex;
    flex-direction: column;
    align-items: center;
    justify-content: center;
    gap: 60px;
  }
  .card {
    width: 740px;
    height: 422px;
    border-radius: 14px;
    background: linear-gradient(160deg, var(--card) 55%, var(--card-shade));
    box-shadow: 0 10px 28px rgba(0,0,0,.18);
    position: relative;
    overflow: hidden;
  }

  /* Front */
  .card-front .brand {
    position: absolute;
    left: 0; right: 0; top: 0; bottom: 66px;
    display: flex;
    align-items: center;
    justify-content: center;
    gap: 22px;
  }
  .brand-dot {
    width: 38px; height: 38px;
    border-radius: 50%;
    background: var(--orange);
    flex: none;
  }
  .brand-name {
    font-size: 58px;
    font-weight: 700;
    letter-spacing: 2px;
    color: var(--grey);
    white-space: nowrap;
  }
  .card-front .web-band {
    position: absolute;
    left: 0; right: 0; bottom: 0;
    height: 66px;
    background: linear-gradient(180deg, var(--orange), var(--orange-deep));
    display: flex;
    align-items: center;
    justify-content: center;
    font-size: 17px;
    font-weight: 700;
    letter-spacing: 2px;
    color: var(--black);
  }

  /* Back */
  .card-back .side-strip {
    position: absolute;
    left: 0; top: 0; bottom: 0;
    width: 46px;
    background: var(--black);
  }
  .card-back .side-strip::before {
    content: "";
    position: absolute;
    left: 0; right: 0; top: 0;
    height: 42%;
    background: var(--orange);
  }
  .card-back .brand {
    position: absolute;
    left: 100px; top: 40px;
    display: flex;
    align-items: center;
    gap: 14px;
  }
  .card-back .brand-dot { width: 26px; height: 26px; }
  .card-back .brand-name { font-size: 38px; letter-spacing: 1px; }
  .details {
    position: absolute;
    left: 100px; top: 140px;
    font-size: 15px;
    line-height: 1.45;
  }
  .person-name {
    color: var(--orange);
    font-weight: 700;
    font-size: 20px;
    letter-spacing: 1px;
  }
  .person-role {
    font-size: 14px;
    font-weight: 700;
    letter-spacing: 1px;
    margin-bottom: 12px;
  }
  .address { margin-bottom: 10px; }
  .contact-list { list-style: none; }
  .contact-list li { display: flex; align-items: center; gap: 8px; }
  .contact-list li::before {
    content: "";
    width: 8px; height: 8px;
    background: var(--orange);
    flex: none;
  }
  .contact-label { color: var(--orange); font-weight: 700; min-width: 34px; }
</style>
</head>
<body>
  <section class="card card-front" aria-label="Business card front">
    <div class="brand">
      <span class="brand-dot"></span>
      <span class="brand-name">Trevik Builders</span>
    </div>
    <div class="web-band">WWW.TREVIKBUILDERS.NET</div>
  </section>

  <section class="card card-back" aria-label="Business card back">
    <div class="side-strip"></div>
    <div class="brand">
      <span class="brand-dot"></span>
      <span class="brand-name">Trevik Builders</span>
    </div>
    <div class="details">
      <p class="person-name">YOUR NAME</p>
      <p class="person-role">POSITION</p>
      <p class="address">PO Box 5087, Corrowen, Qld, 4652</p>
      <ul class="contact-list">
        <li><span class="contact-label">Ph</span>07 4651 2839</li>
        <li><span class="contact-label">Fax</span>07 4651 2840</li>
        <li><span class="contact-label">E</span>trevikbuilders@quillpost.net</li>
        <li><span class="contact-label">ABN</span>47 305 921 276</li>
        <li><span class="contact-label">BSA</span>LIC 6825170</li>
      </ul>
    </div>
  </section>
</body>
</html>
```